lifestyle website Dubai

I need to create a lifestyle website homepage design,

The top nav menu will be:
- Home
- UAE Life
- Emirates Insider
- Career Corner
- HR Essentials
- Blog Beat
- Connect with us

the homepage contents sections will be something like:

- Top Beach Clubs
- Nightlife & Eats
- Outdoor Thrills
- Shopping Spree
- Staycays
- Explore

I've attached an example for the design - but this is not my design so don't copy it.. If you could imagine an Sunwave holiday - Thats the look and feel im after.

```html
<!DOCTYPE html>
<html lang="en">
<head>
<meta charset="utf-8">
<title>Sunwave – Live Work Explore UAE</title>
<link rel="stylesheet" href="https://fonts.googleapis.com/css2?family=Antonio:wght@300;400&family=Poppins:wght@400;500;600&display=swap">
<style>
:root{
  --purple:#4e4a9e;
  --violet:#8b4fb0;
  --pink:#d9519a;
  --teal:#22b3c4;
  --orange:#f7a21b;
  --ink:#151515;
  --muted:#555;
  --paper:#f7f5f2;
  --white:#fff;
}
*{margin:0;padding:0;box-sizing:border-box}
html,body{width:1200px;height:4983px;overflow:hidden}
body{font-family:"Poppins",sans-serif;background:var(--paper);color:var(--ink);position:relative}
.display{font-family:"Antonio",sans-serif;font-weight:300;text-transform:uppercase;letter-spacing:1px}
.abs{position:absolute}
.btn{position:absolute;background:var(--orange);color:var(--ink);font-size:12px;font-weight:600;border-radius:8px;display:flex;align-items:center;justify-content:center;height:42px}
.topbar{top:0;left:0;width:1200px;height:38px;background:var(--purple);color:var(--white);font-size:10px;font-weight:500}
.topbar .hours{left:150px;top:12px}
.topbar .phone{left:372px;top:12px;display:flex;gap:6px;align-items:center}
.socials{display:flex;gap:13px}
.socials span{width:20px;height:20px;border-radius:50%;background:var(--white);display:block}
.topbar .socials{right:148px;top:9px;position:absolute}
.nav{top:38px;left:0;width:1200px;height:88px;background:var(--white)}
.brand{font-family:"Antonio",sans-serif;font-weight:400;color:var(--ink)}
.nav .brand{left:150px;top:22px;font-size:40px}
.nav ul{list-style:none;display:flex;gap:35px;position:absolute;left:310px;top:36px;font-size:12px}
.nav .btn{left:930px;top:22px;width:120px}
.hero{top:126px;left:0;width:1200px;height:674px;background:linear-gradient(80deg,#d65596 0%,#a45bb6 45%,#8c6fbf 70%,#b8a8d8 100%)}
.hero h1{left:150px;top:140px;font-size:66px;line-height:88px;color:var(--white);width:700px}
.hero p{left:150px;top:330px;width:480px;font-size:14px;line-height:25px;color:var(--white)}
.hero .btn{left:150px;top:434px;width:122px;background:var(--white);font-size:11px}
h2.display{position:absolute;width:1200px;text-align:center;font-size:48px;color:var(--ink)}
.accent{color:var(--teal)}
.photo{position:absolute;border-radius:18px}
.club .cap{position:absolute;left:0;bottom:0;width:100%;padding:0 20px 18px;color:var(--white)}
.club .name{font-family:"Antonio",sans-serif;font-size:26px;font-weight:300;display:flex;justify-content:space-between;align-items:center}
.club .ring{width:22px;height:22px;border:1.5px solid var(--white);border-radius:50%}
.club .desc{font-size:10.5px;line-height:19px;margin-top:6px}
.split h2{position:absolute;font-family:"Antonio",sans-serif;font-weight:300;font-size:48px;text-transform:uppercase}
.split .lead{position:absolute;width:450px;font-size:11.5px;line-height:23px;color:var(--ink)}
.split ol{position:absolute;list-style:none;font-size:14px;font-weight:500}
.split li{height:48px;display:flex;gap:14px;align-items:flex-start}
.split li b{width:18px;height:18px;border-radius:50%;background:var(--teal);color:var(--white);font-size:9px;display:flex;align-items:center;justify-content:center;margin-top:2px}
.thrills{top:2048px;left:0;width:1200px;height:697px;background:linear-gradient(90deg,#d5539a 0%,#9a55b0 50%,#c05aa6 100%)}
.tcard{position:absolute;top:184px;width:289px;height:336px;background:var(--white);border-radius:10px}
.tcard .pic{position:absolute;left:12px;top:13px;width:265px;height:232px;border-radius:10px}
.tcard .label{position:absolute;top:270px;width:100%;text-align:center;font-size:18px;font-weight:500}
.tcard .plus{position:absolute;left:128px;bottom:-16px;width:32px;height:32px;border-radius:50%;background:var(--orange);display:flex;align-items:center;justify-content:center;font-weight:600}
.ecard{position:absolute;top:4082px;width:289px;height:303px;background:var(--white);border-radius:6px;box-shadow:0 2px 8px rgba(0,0,0,.08)}
.ecard .pic{position:absolute;left:10px;top:10px;width:269px;height:200px;border-radius:4px}
.ecard h3{position:absolute;top:218px;width:100%;text-align:center;font-size:15px;font-weight:600}
.ecard p{position:absolute;top:246px;left:20px;width:249px;text-align:center;font-size:11.5px;line-height:16px;color:var(--muted)}
.ecard .more{position:absolute;top:285px;width:100%;text-align:center;font-size:10px;font-weight:600}
.footer{top:4548px;left:0;width:1200px;height:435px;background:linear-gradient(90deg,#d5559a 0%,#a459b3 50%,#8f5fb6 100%)}
.footer .brand{left:150px;top:90px;font-size:90px;line-height:110px}
.footer .about{left:150px;top:240px;font-size:14px;line-height:22px;width:340px}
.footer .socials{position:absolute;left:150px;top:306px;gap:20px}
.footer .socials span{width:30px;height:30px;background:var(--orange)}
.fcol{position:absolute;top:162px;font-size:10px;line-height:23px}
.fcol h4{font-size:19px;font-weight:500;margin-bottom:10px}
.footer .rule{left:60px;top:400px;width:1080px;height:1px;background:rgba(0,0,0,.5)}
.footer .bottom{top:410px;font-size:10.5px}
</style>
</head>
<body>

<div class="abs topbar">
  <span class="abs hours">Monday - Friday: 8:00 AM - 9:00 PM</span>
  <span class="abs phone"><svg width="11" height="11" viewBox="0 0 24 24"><path fill="#fff" d="M6.6 10.8a15 15 0 0 0 6.6 6.6l2.2-2.2c.3-.3.7-.4 1-.2 1.1.4 2.3.6 3.6.6.6 0 1 .4 1 1V20c0 .6-.4 1-1 1A17 17 0 0 1 3 4c0-.6.4-1 1-1h3.5c.6 0 1 .4 1 1 0 1.3.2 2.5.6 3.6.1.3 0 .7-.2 1z"/></svg>(555) 014-2290</span>
  <div class="socials"><span></span><span></span><span></span><span></span></div>
</div>

<header class="abs nav">
  <div class="abs brand">SUNWAVE</div>
  <ul><li>Home</li><li>UAE Life</li><li>Emirates Insider</li><li>Career Corner</li><li>HR Essentials</li><li>Blog Beat</li></ul>
  <div class="btn">Contact Us</div>
</header>

<section class="abs hero" role="img" aria-label="Couple in hats overlooking the Dubai skyline with a pink and purple tint">
  <h1 class="abs display">Live Work Explore<br>UAE Your Way</h1>
  <p class="abs">At Palm Tide Collective We Believe That Healing Begins From Within, And That Every Journey Is Unique. Our Mission Is To Provide A Safe And Nurturing</p>
  <div class="btn">Explore Now</div>
</section>

<h2 class="display" style="top:890px">Top <span class="accent">Beach</span> Clubs</h2>
<div class="photo club" style="left:150px;top:1005px;width:289px;height:347px;background:linear-gradient(180deg,#6e8fc4,#7058b0 70%,#5b3fa0)" role="img" aria-label="Jumeirah beach towers with riders in the foreground">
  <div class="cap"><div class="name">Jumeirah Beach<span class="ring"></span></div></div>
</div>
<div class="photo club" style="left:455px;top:1005px;width:289px;height:347px;background:linear-gradient(180deg,#b9cde0,#9fb6cc 35%,#8c6fb6 70%,#6b44a8)" role="img" aria-label="Sandy beach and sea with city towers on the horizon">
  <div class="cap"><div class="name">Market Expansion<span class="ring"></span></div><div class="desc">Our market expansion services leverage deep sector expertise and extensive networks to accelerate the adoption of innovative technologies.</div></div>
</div>
<div class="photo club" style="left:760px;top:1005px;width:289px;height:347px;background:linear-gradient(180deg,#a57dc8,#c78bc0 45%,#8a5cb3 75%,#6b47a6)" role="img" aria-label="Tall tower rising over the city at dusk">
  <div class="cap"><div class="name">Capital Solutions<span class="ring"></span></div></div>
</div>
<div class="btn" style="left:538px;top:1390px;width:122px">Discover More</div>

<section class="split">
  <h2 style="left:150px;top:1526px"><span class="accent">Nightlife</span> &nbsp;&amp;&nbsp; Eats</h2>
  <p class="lead" style="left:150px;top:1610px">At Palm Tide Collective We Believe That Healing Begins From Within, And That Every Journey Is Unique. Our Mission Is To Provide A Safe And Nurturing At Palm Tide Collective</p>
  <ol style="left:150px;top:1714px">
    <li><b>1</b>At Palm Tide Collective We Believe That Healing</li>
    <li><b>2</b>Tide Collective We Believe</li>
    <li><b>3</b>Collective We Believe That Healing</li>
    <li><b>4</b>A Tide Collective We Believe That Healing</li>
  </ol>
  <div class="btn" style="left:150px;top:1913px;width:122px">Learn More</div>
  <div class="photo" style="left:607px;top:1527px;width:443px;height:428px;background:linear-gradient(135deg,#3a2a24,#8a5a3a 50%,#2c2320)" role="img" aria-label="Friends toasting at an outdoor dinner under string lights"></div>
</section>

<section class="abs thrills">
  <h2 class="display" style="top:70px">Outdoor Thrills</h2>
  <div class="tcard" style="left:150px"><div class="pic" style="background:linear-gradient(160deg,#2f7fa8,#1c5c86 60%,#3e9bb0)" role="img" aria-label="Skydiver above the palm-shaped island"></div><div class="label">Skydive</div><div class="plus">+</div></div>
  <div class="tcard" style="left:455px"><div class="pic" style="background:linear-gradient(180deg,#f3b548,#d98a2a 60%,#7a4a1e)" role="img" aria-label="Camel ride across the desert at sunset"></div><div class="label">Dialysis</div><div class="plus">+</div></div>
  <div class="tcard" style="left:760px"><div class="pic" style="background:linear-gradient(180deg,#c9d6e4,#7f8fa8 50%,#4b5a70)" role="img" aria-label="Aerial view of city towers and highways"></div><div class="label">Vascular Imaging</div><div class="plus">+</div></div>
  <div class="btn" style="left:538px;top:582px;width:122px">Discover More</div>
</section>

<h2 class="display" style="top:2836px"><span class="accent">Shopping</span> Spree</h2>
<div class="photo" style="left:67px;top:3048px;width:143px;height:180px;border-radius:6px;background:linear-gradient(180deg,#c8d0e6,#7b6ec2)" role="img" aria-label="Traveller in a sun hat facing the skyline"></div>
<div class="photo" style="left:227px;top:2948px;width:211px;height:322px;border-radius:6px;background:linear-gradient(180deg,#3d5a92,#6a66b8 60%,#5a4aa8)" role="img" aria-label="Traveller walking between modern towers"></div>
<div class="photo" style="left:455px;top:2955px;width:289px;height:362px;border-radius:6px;background:linear-gradient(180deg,#ece8e2,#c9b8a4 40%,#7564b8 85%)" role="img" aria-label="Couple dining on a terrace facing a grand resort"></div>
<div class="photo" style="left:761px;top:3003px;width:211px;height:270px;border-radius:6px;background:linear-gradient(180deg,#aec4de,#8895c8 50%,#5d4fae)" role="img" aria-label="Traveller in a hat looking at the tower skyline"></div>
<div class="photo" style="left:989px;top:3048px;width:143px;height:180px;border-radius:6px;background:linear-gradient(180deg,#d6dcec,#8a7cc6)" role="img" aria-label="Couple with arms raised over the city"></div>

<section class="split">
  <h2 style="left:150px;top:3443px">Staycays</h2>
  <p class="lead" style="left:150px;top:3528px">At Palm Tide Collective We Believe That Healing Begins From Within, And That Every Journey Is Unique. Our Mission Is To Provide A Safe And Nurturing At Palm Tide Collective</p>
  <ol style="left:150px;top:3628px">
    <li><b>1</b>At Palm Tide Collective We Believe That Healing</li>
    <li><b>2</b>Tide Collective We Believe</li>
    <li><b>3</b>Collective We Believe That Healing</li>
    <li><b>4</b>A Tide Collective We Believe That Healing</li>
  </ol>
  <div class="btn" style="left:150px;top:3826px;width:122px">Learn More</div>
  <div class="photo" style="left:607px;top:3443px;width:443px;height:427px;background:linear-gradient(160deg,#d9dde2,#8a8f98 45%,#3c3f47)" role="img" aria-label="Hotel bedroom with a patterned rug and tall window"></div>
</section>

<h2 class="display" style="top:3968px">Explore</h2>
<article class="ecard" style="left:150px"><div class="pic" style="background:linear-gradient(180deg,#cfd9e6,#9aa7b8)" role="img" aria-label="Two people walking beside towers by the water"></div><h3>Board Member Training</h3><p>Lorem Ipsum Dolor Sit Amet Consectetur. Quis Suspendisse A Egestas</p><div class="more">Read More »</div></article>
<article class="ecard" style="left:455px"><div class="pic" style="background:linear-gradient(180deg,#d6dde6,#7f9070 70%,#a89888)" role="img" aria-label="Person walking along a palm-lined promenade"></div><h3>Software Transition</h3><p>Lorem Ipsum Dolor Sit Amet Consectetur. Quis Suspendisse A Egestas</p><div class="more">Read More »</div></article>
<article class="ecard" style="left:760px"><div class="pic" style="background:linear-gradient(180deg,#9fc6dc,#3d8fb0 60%,#e0a460)" role="img" aria-label="Woman with a drink at a marina table"></div><h3>Leadership Coaching</h3><p>Lorem Ipsum Dolor Sit Amet Consectetur. Quis Suspendisse A Egestas</p><div class="more">Read More »</div></article>
<div class="btn" style="left:542px;top:4450px;width:116px">Discover More</div>

<footer class="abs footer">
  <div class="abs brand">SUNWAVE</div>
  <p class="abs about">Lorem Ipsum Dolor Amet Consectetur. Mauris Enim Dapibus Mauris Leo</p>
  <div class="socials"><span></span><span></span><span></span><span></span></div>
  <div class="fcol" style="left:592px"><h4>Services</h4>Lorem Ipsum Dolor<br>Amet Consectetur<br>Mauris Enim<br>Dapibus Mauris</div>
  <div class="fcol" style="left:768px"><h4>Used Full Links</h4>Lorem Ipsum Dolor Amet<br>Consectetur. Mauris Enim<br>Dapibus Mauris</div>
  <div class="fcol" style="left:985px"><h4>Legal</h4>Terms Of Use<br>Privacy Policy<br>Cookie Policy</div>
  <div class="abs rule"></div>
  <div class="abs bottom" style="left:60px">Copyright © 2025 All Right Reserved</div>
  <div class="abs bottom" style="left:797px">Privacy Policy</div>
  <div class="abs bottom" style="left:901px">Terms Of Service</div>
  <div class="abs bottom" style="left:1024px">Cookies Settings</div>
</footer>

</body>
</html>
```